Web Design Project

Hi,
I am building a web based business within the wedding industry and I am looking for someone to design the front page of the website for me as well as the following pages/categroires which all need to be supportive of the front page
The screens will be:
Home
One Stop Reistry
Wedding Deals
Travel/Getaway
Wedding marketplace
Blog
Contact US
A more detailed view of the above is as follows:
1. Home page - be bright and capture an audience
2. Aggregate gift registries ie from key online retailers so people visiting my site can set up a bridal registry from numerous stores all in the one place ie: http://www.harlowbrent.com.au/, http://www.quillo.com.au/, http://www.kvsonic.com.au/ http://www.felixramsay.com.au/ Something similar to http://www.vowpresentsnow.com.au
3. Aggregate the deal sites to pull all the deals relating to weddings ie: hair and make up, travel, car hire, venue hire, waxing, laser, facials, beauty treatments. Similar to http://www.pennysaverhub.com.au/daily-deals or http://www.ringbargains.com.au/
3. We will have a tab for travel and accommodation which we want to pull the info from Voyaro which I believe you can become a member and do so quite easily http://www.voyaro.com.au/daily/service/affiliate-program.aspx
4. We want to build like our own tradlo/marketplace within the site where people can list things like their wedding dress, gifts they don’t want or need etc similar to http://www.gownagain.com/
5. A blog tab where we can have blogs/gossip section and build a forum for people to discuss wedding related issues similar to http://www.altartalk.com/wedding-forums or http://veilnest.com.au/Forums or gossip like http://www.starlettechatter.com/categories/celebrity-weddings/ The look of this section could be designed to look a bit like a gossip magazine
People need to be able to log in and out of the site and it needs to be able to be connected with pallbook and workvine as well as allowing people to subscribe to a mailing list and unsubscribe if required.
I have done a quick mock-up on powerpoint with what needs to be included but needs a lot of changing. Can be any pictures and what I have attached is not an ide ajust essentials to be on the page.
A good site to give you an idea is http://thebouquet.sevenweb.com.au/

```html
<!DOCTYPE html>
<html lang="en">
<head>
<meta charset="utf-8">
<title>Vow Glimmer</title>
<link rel="stylesheet" href="https://fonts.googleapis.com/css2?family=Quicksand:wght@400;500;600&display=swap">
<style>
  :root {
    --blush: #fde3e8;
    --blush-deep: #fbd0da;
    --rose: #f28fa9;
    --rose-dark: #e0607e;
    --rose-text: #de6d8a;
    --brand: #c45f74;
    --panel-top: #fde2e8;
    --panel-bottom: #f8b0c1;
    --button-top: #f6c4d1;
    --button-bottom: #c9849c;
    --ink: #3a2a2e;
    --white: #ffffff;
    --field-text: #6a6a6a;
  }
  * { box-sizing: border-box; margin: 0; padding: 0; }
  html, body { width: 1200px; height: 948px; overflow: hidden; }
  body {
    position: relative;
    font-family: "Quicksand", sans-serif;
    color: var(--ink);
    background: linear-gradient(160deg, #fdeef1 0%, var(--blush) 45%, var(--blush-deep) 100%);
  }
  .brand {
    position: absolute; left: 22px; top: 22px;
    font-family: "Quicksand", sans-serif; font-weight: 600;
    font-size: 40px; letter-spacing: 2px; line-height: 50px;
    color: var(--brand);
  }
  .quote-button {
    position: absolute; left: 1042px; top: 32px; width: 139px; height: 42px;
    background: linear-gradient(var(--button-top), var(--button-bottom));
    border: 1px solid #f5d5dd;
    color: var(--white); font-family: Arial, sans-serif; font-style: italic;
    font-size: 29px; text-align: center; line-height: 40px;
  }
  .main-nav {
    position: absolute; left: 20px; top: 85px; width: 1161px; height: 81px;
    background: var(--white); border-top: 5px solid var(--rose);
  }
  .main-nav a {
    position: absolute; top: 14px;
    color: var(--rose-text); text-decoration: none; font-size: 19px; line-height: 24px;
  }
  .main-nav .home-tab {
    left: 0; top: -5px; width: 119px; height: 81px;
    background: #fcd6df; color: var(--ink);
    display: flex; align-items: center; justify-content: center;
  }
  .hero-photo {
    position: absolute; left: 20px; top: 185px; width: 807px; height: 594px;
    background: linear-gradient(180deg, #c9def1 0%, #eef3f7 45%, #dedfe2 62%, #8d8f94 100%);
  }
  .side-panel {
    position: absolute; left: 841px; width: 340px;
    background: linear-gradient(var(--panel-top), var(--panel-bottom));
  }
  .panel-title { position: absolute; left: 22px; color: var(--rose-dark); font-weight: 600; }
  .field {
    position: absolute; left: 22px; width: 299px; height: 34px;
    background: var(--white); color: var(--field-text);
    font-family: Arial, sans-serif; font-style: italic; font-size: 15px;
    padding-left: 11px; line-height: 34px;
  }
  .pink-button {
    position: absolute; height: 32px;
    background: linear-gradient(var(--button-top), var(--button-bottom));
    border: 1px solid #f6d8df;
    color: var(--white); font-weight: 600; font-size: 17px; text-align: center; line-height: 30px;
  }
  .account-links { position: absolute; left: 22px; top: 166px; color: var(--white); font-size: 15px; line-height: 19px; }
  .social-square {
    position: absolute; left: 26px; top: 21px; width: 43px; height: 43px;
    border-radius: 6px; background: #f9c6d3; border: 1px solid #f2a9bb;
  }
  .social-label { position: absolute; left: 85px; top: 30px; color: #e98aa3; font-size: 18px; }
  .footer-band {
    position: absolute; left: 20px; top: 802px; width: 1161px; height: 69px;
    background: var(--rose);
  }
  .footer-band a {
    position: absolute; top: 24px; color: var(--ink); text-decoration: none; font-size: 15px;
  }
  .copyright {
    position: absolute; left: 0; top: 895px; width: 1200px; text-align: center;
    font-size: 12.5px; color: var(--ink);
  }
</style>
</head>
<body>
  <header>
    <div class="brand">Vow Glimmer</div>
    <a class="quote-button">Quote</a>
  </header>

  <nav class="main-nav">
    <a class="home-tab">Home</a>
    <a style="left:147px">One Stop<br>Registry</a>
    <a style="left:297px">Wedding<br>Deals</a>
    <a style="left:446px">Travel/Accommodation<br>Gateway</a>
    <a style="left:730px">Wedding<br>Marketplace</a>
    <a style="left:904px">Gossip/<br>Editorial</a>
    <a style="left:1059px">Booking<br>Engine</a>
  </nav>

  <div class="hero-photo" role="img" aria-label="Photo of a white rose bridal bouquet on a boardwalk with a couple in the soft-focus background"></div>

  <section class="side-panel sign-in" style="top:186px;height:220px">
    <h2 class="panel-title" style="top:20px;font-size:23px">Sign In</h2>
    <div class="field" style="top:59px">Username</div>
    <div class="field" style="top:121px">Password</div>
    <div class="account-links">Join Now<br>Forgotten Password?</div>
    <a class="pink-button" style="left:241px;top:168px;width:80px">Sign In</a>
  </section>

  <section class="side-panel social-link" style="top:415px;height:85px">
    <span class="social-square"></span>
    <span class="social-label">Join Our Pallbook Group</span>
  </section>

  <section class="side-panel social-link" style="top:507px;height:85px">
    <span class="social-square"></span>
    <span class="social-label">Follow us on chirpa</span>
  </section>

  <section class="side-panel mailing-list" style="top:601px;height:178px">
    <h2 class="panel-title" style="top:23px;font-size:19px;letter-spacing:0.5px">Subscribe to Our Mailing List</h2>
    <div class="field" style="top:73px">Enter your email id</div>
    <a class="pink-button" style="left:224px;top:120px;width:97px">Submit</a>
  </section>

  <footer>
    <nav class="footer-band">
      <a style="left:56px">About Vow Glimmer</a>
      <a style="left:328px">Adertise with us</a>
      <a style="left:549px">Contact us</a>
      <a style="left:733px">Terms &amp; Conditions</a>
      <a style="left:981px">Privacy Policy</a>
    </nav>
    <p class="copyright">© 2012 Vow Glimmer - Terms of Service - Privacy Policy - Program Policies</p>
  </footer>
</body>
</html>
```